Personal contact Business card design needed

I work in the Property Industry - specifically Property Management.

I need a card I can hand out to colleagues at networking events, meetings, training courses etc. that will provide my contact details.

Target Market(s)

Professional colleagues / potential clients / employers

Industry/Entity Type

Training

Contact Information for Business Card

I need a simple and professional card to give to professional network contacts at meetings, interviews etc.

The card should include my photograph, name, mobile number, email address and Proflinx address.

I would like appropriate professional colours. Something feminine but not too 'frilly' or 'girly'

Requirements
Must have
• Photograph of myself.
I want it to be simple,perhaps a small icon for each contact detail such as
Email icon
Proflinx icon
Mobile number

```html
<!DOCTYPE html>
<html lang="en">
<head>
<meta charset="utf-8">
<title>Property Management – Business Card</title>
<link rel="stylesheet" href="https://fonts.googleapis.com/css2?family=Marcellus&family=Poiret+One&display=swap">
<style>
  :root {
    --page-bg: #e9e6e8;
    --magenta-light: #c0479e;
    --magenta: #a8338a;
    --magenta-deep: #8e2474;
    --swoosh-grey: #6f6f72;
    --swoosh-light: #b9b9bc;
    --card-white: #ffffff;
    --text-white: #ffffff;
    --icon-grey: #d9d3d8;
    --icon-dark: #5a4a56;
  }
  * { margin: 0; padding: 0; box-sizing: border-box; }
  html, body {
    width: 1200px;
    height: 675px;
    overflow: hidden;
    background: var(--page-bg);
  }
  .business-card {
    position: absolute;
    left: 100px;
    top: 52px;
    width: 1000px;
    height: 570px;
    background: var(--card-white);
    box-shadow: 0 6px 22px rgba(0, 0, 0, 0.18);
    overflow: hidden;
  }
  .card-shape {
    position: absolute;
    inset: 0;
    width: 1000px;
    height: 570px;
  }
  .backdrop-image {
    position: absolute;
    left: 370px;
    top: 10px;
    width: 260px;
    height: 270px;
    border-radius: 50%;
    background: radial-gradient(circle, rgba(230, 190, 220, 0.22) 0%, rgba(200, 120, 180, 0.1) 50%, rgba(168, 51, 138, 0) 72%);
  }
  .title {
    position: absolute;
    font-family: "Poiret One", "Marcellus", sans-serif;
    color: var(--text-white);
    font-size: 46px;
    letter-spacing: 1px;
    line-height: 1;
    white-space: nowrap;
    text-shadow: 2px 2px 2px rgba(60, 0, 40, 0.55);
  }
  .title-property { left: 160px; top: 36px; }
  .title-management { left: 388px; top: 62px; }
  .contact {
    position: absolute;
    display: flex;
    align-items: center;
    gap: 10px;
    font-family: "Marcellus", serif;
    color: var(--text-white);
    font-size: 20px;
    line-height: 1;
    white-space: nowrap;
    text-shadow: 1px 1px 1px rgba(60, 0, 40, 0.35);
  }
  .contact-name { left: 80px; top: 150px; }
  .contact-phone { left: 74px; top: 190px; }
  .contact-email { left: 503px; top: 146px; }
  .contact-profile { left: 496px; top: 200px; font-size: 18px; }
  .phone-spacer { width: 16px; }
  .icon { flex: none; display: block; }
  .portrait {
    position: absolute;
    left: 340px;
    top: 200px;
    width: 235px;
    height: 180px;
    border-radius: 110px 110px 0 0;
    background: linear-gradient(180deg, #5b3a3c 0%, #3a2a2e 55%, #1f1a1d 100%);
  }
</style>
</head>
<body>
  <main class="business-card">
    <svg class="card-shape" viewBox="0 0 1000 570" aria-hidden="true">
      <defs>
        <linearGradient id="panel-gradient" x1="0" y1="0" x2="1" y2="1">
          <stop offset="0" stop-color="var(--magenta-light)"/>
          <stop offset="0.5" stop-color="var(--magenta)"/>
          <stop offset="1" stop-color="var(--magenta-deep)"/>
        </linearGradient>
      </defs>
      <path class="swoosh-light" d="M0 288 Q500 506 1000 278 V288 Q500 518 0 298 Z" fill="var(--swoosh-light)"/>
      <path class="swoosh-dark" d="M0 280 Q500 496 1000 270 V280 Q500 508 0 290 Z" fill="var(--swoosh-grey)"/>
      <path class="magenta-panel" d="M0 0 H1000 V270 Q500 490 0 280 Z" fill="url(#panel-gradient)"/>
    </svg>

    <div class="backdrop-image" role="img" aria-label="Faint background photo of a house"></div>

    <h1 class="title title-property">PROPERTY</h1>
    <p class="title title-management">MANAGEMENT</p>

    <p class="contact contact-name">Name: Jane Lowe</p>

    <p class="contact contact-phone">
      <svg class="icon" width="36" height="46" viewBox="0 0 42 52" aria-hidden="true">
        <rect x="6" y="2" width="30" height="48" rx="6" fill="var(--icon-grey)" stroke="var(--icon-dark)" stroke-width="2" transform="rotate(-18 21 26)"/>
        <rect x="11" y="9" width="20" height="30" rx="2" fill="var(--icon-dark)" transform="rotate(-18 21 26)"/>
      </svg>
      <span class="phone-spacer"></span>
      <span>: 0400 512 389</span>
    </p>

    <div class="portrait" role="img" aria-label="Head-and-shoulders photograph of the card holder"></div>

    <p class="contact contact-email">
      <svg class="icon" width="28" height="26" viewBox="0 0 30 28" aria-hidden="true">
        <rect x="1" y="1" width="28" height="26" rx="3" fill="var(--icon-grey)"/>
        <rect x="5" y="8" width="20" height="13" fill="var(--icon-dark)"/>
        <path d="M5 8 L15 16 L25 8" fill="none" stroke="var(--icon-grey)" stroke-width="2"/>
      </svg>
      <span>: jane@mailbox-example.com.au</span>
    </p>

    <p class="contact contact-profile">
      <svg class="icon" width="28" height="24" viewBox="0 0 30 26" aria-hidden="true">
        <rect x="1" y="1" width="28" height="24" rx="3" fill="var(--icon-grey)"/>
      </svg>
      <span>: au.proflinx.com/in/janeloweaustralia</span>
    </p>
  </main>
</body>
</html>
```